Book cover - Quiet Rooms, Open Doors

Book cover for Ebook (Pagelight) and wrap around print cover (Printvale) (back, front, and spine)

The book title (may slightly change by end of brief):
(MAIN TITLE) 'Quiet Rooms, Open Doors'
(SUB HEADING) 'A Week-by-Week Practical Workbook to Loosen Nervous Habits, Quieten Doubt and Build Steady Poise'
by Dr Owen Hartley

I would like a bold, stand out cover. Contemporary. I would like to avoid stereotypical images of people looking anxious or worried. I would like the design to be more uplifting and hopeful, rather than focusing on the negative aspect of anxiety, but avoiding cliched photos of people raising their hands in the air, smiling and jumping etc. The cover should appeal to both men and women.

Trim size of book cover (for PrintVale) is 5.25" x 8" back and front with a spine size of 0.477 inches

Reason: I have decided to extend the deadline by 1 more day, not because I am unhappy with the quality of the designs, but because a few designers have contacted me to explain they have had technical difficulties when submitting their files. Thanks everyone for the hard work and great designs.

Target Market(s)

Males and females (16+) who struggle with social anxiety and shyness

Industry/Entity Type

Social

Font styles to use
Serif

Requirements
Must have
• Bold cover that is modern and contemporary. For example, I like these covers:
• http://shrtlnk.example/k4Tq9Zb
• http://shrtlnk.example/m8Wv2Hn
• http://shrtlnk.example/p3Jx6Lr
• http://shrtlnk.example/t7Gd1Qe
• http://shrtlnk.example/v2Nk8Fy
• http://shrtlnk.example/w9Bh4Cs
• http://shrtlnk.example/z5Mf3Ud
Nice to have
• Open to abstract designs.
Should not have
• No stereotypical pictures of people who look anxious or worried. Avoid cliched photos of people raising their hands in the air, smiling and jumping etc.

```html
<!DOCTYPE html>
<html lang="en">
<head>
<meta charset="utf-8">
<title>Quiet Rooms, Open Doors — Book Cover</title>
<link href="https://fonts.googleapis.com/css2?family=Dancing+Script:wght@600&family=Patrick+Hand&family=Lilita+One&display=swap" rel="stylesheet">
<style>
  :root {
    --page-bg: #e9eaea;
    --leaf-deep: #1f4a12;
    --leaf-mid: #3f8a1f;
    --leaf-bright: #7cc23a;
    --glow: #f4ffb0;
    --meadow: #8fcf5a;
    --ink-light: #ffffff;
    --title-shadow: rgba(20, 40, 10, 0.75);
  }
  * { margin: 0; padding: 0; box-sizing: border-box; }
  html, body {
    width: 1200px;
    height: 800px;
    overflow: hidden;
    background: var(--page-bg);
  }
  .cover {
    position: absolute;
    left: 364px;
    top: 40px;
    width: 472px;
    height: 720px;
    overflow: hidden;
    box-shadow: 0 6px 24px rgba(0, 0, 0, 0.18);
  }
  .cover-art {
    position: absolute;
    inset: 0;
    background:
      radial-gradient(ellipse 70px 90px at 52% 46%, var(--glow) 0%, rgba(244,255,176,0.6) 45%, rgba(244,255,176,0) 100%),
      radial-gradient(ellipse 150px 200px at 50% 48%, rgba(170,220,70,0.85) 0%, rgba(120,190,50,0.3) 60%, rgba(0,0,0,0) 100%),
      linear-gradient(180deg, rgba(0,0,0,0) 55%, var(--meadow) 78%, #a6d873 100%),
      radial-gradient(ellipse at 50% 40%, var(--leaf-bright) 0%, var(--leaf-mid) 45%, var(--leaf-deep) 100%);
  }
  .author {
    position: absolute;
    top: 16px;
    left: 0;
    width: 100%;
    text-align: center;
    font-family: "Dancing Script", cursive;
    font-weight: 600;
    font-size: 26px;
    color: var(--ink-light);
    text-shadow: 0 1px 3px var(--title-shadow);
  }
  .subtitle {
    position: absolute;
    top: 56px;
    left: 30px;
    width: 420px;
    font-family: "Patrick Hand", cursive;
    font-size: 15px;
    line-height: 1.45;
    text-transform: uppercase;
    letter-spacing: 0.3px;
    color: var(--ink-light);
    text-shadow: 0 1px 2px var(--title-shadow);
  }
  .subtitle span { display: block; }
  .title {
    position: absolute;
    top: 470px;
    left: 0;
    width: 100%;
    text-align: center;
    font-family: "Lilita One", sans-serif;
    font-weight: 400;
    color: var(--ink-light);
    text-transform: uppercase;
    line-height: 1;
    text-shadow: 2px 3px 5px var(--title-shadow);
  }
  .title span { display: block; }
  .title .title-lead { font-size: 66px; }
  .title .title-mid { font-size: 42px; margin-top: 4px; }
  .title .title-small { font-size: 36px; margin-top: 4px; }
  .title .title-end { font-size: 68px; margin-top: 4px; }
</style>
</head>
<body>
  <div class="cover">
    <div class="cover-art" role="img" aria-label="Illustration of a small white mouse stepping out of a glowing tunnel of green leaves onto a grassy path"></div>
    <p class="author">Dr Owen Hartley</p>
    <p class="subtitle">
      <span>A Week-by-Week Practical Workbook</span>
      <span>to Loosen Nervous Habits,</span>
      <span>Quieten Doubt</span>
      <span>and Build Steady Poise</span>
    </p>
    <h1 class="title">
      <span class="title-lead">Quiet</span>
      <span class="title-mid">Rooms,</span>
      <span class="title-small">Open</span>
      <span class="title-end">Doors</span>
    </h1>
  </div>
</body>
</html>
```